Maple Crest Venture Fund

Take current power point presentation and make it uniform in color and font, and create designs that pop throughout the presentation. Right now, it is dull and mundane.

```html
<!DOCTYPE html>
<html lang="en">
<head>
<meta charset="utf-8">
<title>Maple Crest Venture Fund – Presentation</title>
<link href="https://fonts.googleapis.com/css2?family=Poppins:wght@300;400;500;600;700&display=swap" rel="stylesheet">
<style>
:root{
  --blue:#1168b5;
  --blue-title:#1572bf;
  --band:#1a6fbd;
  --col:#2b87cf;
  --col-head:#1c79c4;
  --ink:#333b44;
  --rule:#3c3f44;
  --sep:#5a5d62;
  --frame:#d9dde2;
}
*{box-sizing:border-box;margin:0;padding:0}
html,body{width:1200px;height:3404px;overflow:hidden;background:#fff}
body{position:relative;font-family:'Poppins',sans-serif;color:var(--ink)}
.abs{position:absolute}
.slide-title{position:absolute;left:75px;font-weight:600;color:var(--blue-title);font-size:29px;line-height:1.2}
.title-rule{position:absolute;left:75px;height:5px;background:var(--rule)}
.photo{position:absolute}
.name-band{position:absolute;left:0;right:0;bottom:0;background:var(--band);color:#fff;font-weight:600;font-size:20px;text-align:center;display:flex;align-items:center;justify-content:center}
.bio{position:absolute;left:330px;width:830px;border:2px solid var(--frame);box-shadow:3px 3px 0 #e6e9ec;padding:22px 40px 0 42px;font-weight:300;font-size:16.3px;line-height:25.3px;color:#2f3640}
.bio p+p{margin-top:5px}
.note{position:absolute;left:0;width:1200px;text-align:center;font-size:11.3px;color:#222}
.note em{font-style:italic}
.separator{position:absolute;left:0;width:1200px;height:5px;background:var(--sep)}
.subtitle{position:absolute;left:75px;top:1500px;font-weight:600;font-size:22px;color:var(--blue-title)}
.pillar{position:absolute;top:1545px;height:428px;background:var(--col);color:#fff}
.pillar h3{height:37px;background:var(--col-head);font-weight:600;font-size:17px;display:flex;align-items:center;justify-content:center;border-bottom:3px solid #fff}
.pillar ul{padding:20px 16px 0 40px;font-size:16px;line-height:23.4px;font-weight:400}
.pillar li{margin-bottom:10px}
.pillar li::marker{font-size:11px}
.brand{position:absolute;left:660px;top:2185px;width:240px;text-align:center;color:var(--blue);font-weight:700;font-size:28px;line-height:1.15}
.agenda{position:absolute;left:614px;top:2302px;width:470px;height:321px;border:2px solid var(--frame);box-shadow:3px 3px 0 #e6e9ec;padding:28px 30px 0 50px}
.agenda h2{font-weight:600;font-size:22px;color:var(--blue-title);margin-bottom:8px}
.agenda ul{padding-left:20px;font-size:17.5px;line-height:27.2px;font-weight:400;color:#333}
.why-title{position:absolute;left:531px;top:2832px;font-weight:600;font-size:31px;line-height:42px;color:var(--blue-title)}
.why-sub{position:absolute;left:538px;top:2933px;font-weight:600;font-size:22px;color:var(--blue-title)}
.advantages{position:absolute;left:574px;top:2975px;width:510px;padding-left:0;font-size:20.5px;line-height:31px;font-weight:400;color:#2b2f35}
.advantages li{margin-bottom:0}
</style>
</head>
<body>

<!-- Senior management: founders -->
<h1 class="slide-title" style="top:62px">Senior Management</h1>
<div class="title-rule" style="top:106px;width:355px"></div>

<div class="photo" style="left:75px;top:151px;width:236px;height:216px;background:linear-gradient(160deg,#2c3848,#6b5548 55%,#1d2633)" role="img" aria-label="Portrait photo of Daniel Reyes">
  <div class="name-band" style="height:37px">Daniel Reyes</div>
</div>
<div class="bio" style="top:149px;height:224px">
  <p>Daniel Reyes is a Founder and Member of Maple Crest Investments LLC, bringing over 17 years of experience in PIPE (Private Investment in Public Equity) transactions. Prior to launching his own funds, Mr. Reyes co-founded multiple investment funds and managed portfolios for a boutique family of funds. Before joining the family of funds in 2009, he worked as an analyst for an $800 million hedge fund based in Long Island, New York, where he oversaw fifty-five portfolio companies with a focus on private equity financing. Mr. Reyes holds a Bachelor of Arts in Finance from Northfield State University.</p>
</div>

<div class="photo" style="left:75px;top:390px;width:236px;height:218px;background:linear-gradient(180deg,#eef0f2,#c9ccd0 55%,#2b3038)" role="img" aria-label="Portrait photo of Omar Castell">
  <div class="name-band" style="height:38px">Omar Castell</div>
</div>
<div class="bio" style="top:387px;height:225px">
  <p>Omar Castell is a Founder and Member of Maple Crest Investments LLC with extensive experience investing in publicly traded companies since 2011. In addition to co-founding multiple investment funds, Mr. Castell’s professional background spans roles at a New York State Agency, a class action administration firm, and an I.T. company prior to his transition into finance. Mr. Castell earned his Juris Doctor (J.D.) from Eastbrook University and holds a Bachelor’s degree in Philosophy, Politics, and Law from Northfield State University.</p>
</div>

<p class="note" style="top:629px">Please refer to the page entitled <em>“General Notes and Risk Factors” when reviewing the information presented herein.</em></p>
<div class="separator" style="top:676px"></div>

<!-- Senior management: executive -->
<h1 class="slide-title" style="top:744px">Senior Management</h1>
<div class="title-rule" style="top:788px;width:355px"></div>

<div class="photo" style="left:75px;top:895px;width:236px;height:322px;background:linear-gradient(165deg,#4a4036,#8c7868 50%,#2a2a30)" role="img" aria-label="Portrait photo of Peter Hallam">
  <div class="name-band" style="height:47px">Peter Hallam</div>
</div>
<div class="bio" style="top:826px;height:460px;padding-top:20px">
  <p>Peter Hallam is a business executive with extensive C-level and Board of Director leadership experience across multiple privately and publicly held companies. He is currently a Founder and Member of Maple Crest Investments LLC. Previously, Mr.</p>
  <p>Hallam was the Founder, Chairman, and Chief Executive Officer of Lifeline Cell Bank, Inc. (LCBI), a company specializing in harvesting and storing stem cells in the U.S. and internationally, from 2003 to 2012. He also concurrently served as CEO and Chairman of Lifeline Partners Inc., later absorbed by LCBI in 2005, and as Founder and President of Northern Stem Cells, Inc., a stem cell storage facility in northeastern China.</p>
  <p>Before joining MCVF, Mr. Hallam worked as a licensed investment banker with Harborline Securities, LLC, providing microcap advisory and capital introduction services to publicly traded companies. In this role, he cultivated relationships with hedge funds, venture capital funds, family offices, and other institutional investors.</p>
  <p>Mr. Hallam currently serves on the Special Council of the Civic Defense Council and has previously held leadership positions as Chairman of the Regional Development Authority Biotech Committees and as a board member of the Desert Natural History Museum. He holds a Bachelor of Arts in Biology from Bayview College.</p>
</div>

<p class="note" style="top:1311px">Please refer to the page entitled <em>“General Notes and Risk Factors” when reviewing the information presented herein.</em></p>
<div class="separator" style="top:1358px"></div>

<!-- Competitive advantage -->
<h1 class="slide-title" style="top:1426px;font-size:31px">MCVF’s Competitive Advantage</h1>
<div class="title-rule" style="top:1470px;width:507px"></div>
<p class="subtitle">A Leading direct investment fund in a growing sector with beneficial liquidity terms.</p>

<section class="pillar" style="left:82px;width:284px">
  <h3>People</h3>
  <ul>
    <li>Tight and established team and infrastructure. Additional use of outside professionals for reduced overhead and access to top talent.</li>
    <li>Specialized experience with collateralized investments.</li>
    <li>The members have invested or been involved with over $100 million for over 11 years through various market cycles.</li>
  </ul>
</section>
<section class="pillar" style="left:378px;width:226px">
  <h3>Process</h3>
  <ul>
    <li>Proven and rigorous due diligence, portfolio construction and risk management processes.</li>
  </ul>
</section>
<section class="pillar" style="left:616px;width:244px">
  <h3>Philosophy</h3>
  <ul>
    <li>To pair our rigorous diligence processes, with a disciplined investment approach and strong management to facilitate consistent performance.</li>
  </ul>
</section>
<section class="pillar" style="left:872px;width:246px">
  <h3>Performance</h3>
  <ul>
    <li>Consistent annual returns since inception (2015).</li>
    <li>Long-term track record of performance by the Members.</li>
  </ul>
</section>

<p class="note" style="top:1993px">Please refer to the page entitled <em>“General Notes and Risk Factors” when reviewing the information presented herein.</em></p>
<div class="separator" style="top:2040px"></div>

<!-- Section divider: why direct investments -->
<div class="photo" style="left:0;top:2045px;width:465px;height:680px;background:linear-gradient(120deg,#6d7f93,#b9c3cd 45%,#2c3a52 75%,#1f2a3e)" role="img" aria-label="Photo of a smiling businesswoman in a navy blazer with arms crossed"></div>
<div class="abs" style="left:465px;top:2045px;width:27px;height:680px;background:var(--band)"></div>

<div class="brand">Maple Crest<br>Venture Fund</div>

<div class="agenda">
  <h2>Why Direct Investments?</h2>
  <ul>
    <li>Why MCVF’s Direct Investment Strategy?</li>
    <li>Industry Overview</li>
    <li>Differentiation Between PIPE’s and Direct Investments</li>
    <li>Capital/Deal Structure</li>
    <li>How We Make Money</li>
    <li>Process</li>
    <li>Protection/Risk</li>
  </ul>
</div>
<p class="note" style="left:640px;width:400px;top:2664px;line-height:15px">Please refer to the page entitled <em>“General Notes and Risk Factors” when reviewing the information presented herein.</em></p>
<div class="separator" style="top:2723px"></div>

<!-- Why direct strategy -->
<div class="photo" style="left:58px;top:2782px;width:385px;height:555px;background:linear-gradient(160deg,#0e1a26,#1d3650 50%,#0a1219)" role="img" aria-label="Photo of a businessman in a navy suit adjusting his wristwatch"></div>
<div class="abs" style="left:443px;top:2782px;width:20px;height:555px;background:var(--band)"></div>

<h1 class="why-title">Why MCVF’s Direct<br>Investment Strategy?</h1>
<div class="title-rule" style="left:531px;top:2912px;width:365px"></div>
<p class="why-sub">Key Advantages</p>
<ul class="advantages">
  <li>Upside Potential – through strategic investments.</li>
  <li>Risk Management: Achieved through tranching strategies.</li>
  <li>Equity Kickers: Warrants or stock provide additional upside potential.</li>
  <li>Market Arbitrage/ Appreciation: Participation at a fixed discount at funding allowing arbitrage at.</li>
  <li>Robust Deal Flow: Access to a vast pipeline of deals within various sectors.</li>
</ul>

<p class="note" style="top:3358px">Please refer to the page entitled <em>“General Notes and Risk Factors” when reviewing the information presented herein.</em></p>

</body>
</html>
```